For a German comparison website comparing the best online trading brokers I need 10 banners for Facebook advertising. The banners should be a size of 1200x628 with one of the following texts:
1) Traden für Anfänger
25 Euro gratis
2) Traden Sie online
25 Euro gratis
3) Online-Trading für Anfänger
4) Trading für Einsteiger
25 Euro gratis
5) Aktien für Einsteiger
25 Euro gratis
The targeted website is www.borsivolta.ch and it compares brokers where traders can trade shares, commodities,indices and Forex.

```html
<!DOCTYPE html>
<html lang="de">
<head>
<meta charset="utf-8">
<title>Traden für Anfänger – 25 Euro gratis</title>
<link rel="stylesheet" href="https://fonts.googleapis.com/css2?family=Cinzel:wght@400;600&display=swap">
<style>
  :root {
    --navy-deep: #0b2f57;
    --navy: #134476;
    --navy-light: #3f6e9c;
    --ribbon: rgba(128, 140, 152, 0.82);
    --ribbon-edge: rgba(200, 210, 220, 0.55);
    --text-light: #ffffff;
    --gold-light: #ddd5a0;
    --gold: #c8bd80;
    --gold-edge: #3a3522;
    --text-dark: #15140f;
    --globe-light: #4f93d6;
    --globe-dark: #0c3f8f;
  }
  html, body {
    margin: 0;
    padding: 0;
    width: 1200px;
    height: 628px;
    overflow: hidden;
  }
  .banner {
    position: relative;
    width: 1200px;
    height: 628px;
    overflow: hidden;
    background: linear-gradient(180deg, var(--navy) 0%, var(--navy-deep) 55%, var(--navy) 100%);
    font-family: "Cinzel", "Times New Roman", serif;
  }
  .backdrop {
    position: absolute;
    inset: 0;
  }
  .globe {
    position: absolute;
    left: 730px;
    top: 120px;
    width: 540px;
    height: 540px;
    border-radius: 50%;
    background: radial-gradient(circle at 45% 45%, var(--globe-light) 0%, #2a6fc0 45%, var(--globe-dark) 100%);
    box-shadow: 0 0 0 14px rgba(150, 190, 235, 0.35);
  }
  .ribbon {
    position: absolute;
    left: -30px;
    top: 30px;
    width: 900px;
    height: 118px;
    background: var(--ribbon);
    border-top: 2px solid var(--ribbon-edge);
    border-bottom: 2px solid var(--ribbon-edge);
    transform-origin: 0 0;
    transform: rotate(5.6deg);
    box-shadow: 0 6px 18px rgba(0, 0, 0, 0.35);
  }
  .ribbon-title {
    margin: 0;
    padding-left: 62px;
    line-height: 118px;
    font-size: 74px;
    font-weight: 400;
    color: var(--text-light);
    letter-spacing: 0.5px;
    white-space: nowrap;
    text-shadow: 2px 3px 4px rgba(0, 0, 0, 0.55);
  }
  .offer-badge {
    position: absolute;
    left: 550px;
    top: 245px;
    width: 250px;
    height: 235px;
  }
  .offer-badge text {
    font-family: "Cinzel", "Times New Roman", serif;
    fill: var(--text-dark);
    font-size: 46px;
  }
</style>
</head>
<body>
<main class="banner">
  <svg class="backdrop" width="1200" height="628" viewBox="0 0 1200 628" aria-hidden="true">
    <defs>
      <filter id="soft" x="-20%" y="-50%" width="140%" height="200%">
        <feGaussianBlur stdDeviation="10"/>
      </filter>
    </defs>
    <ellipse cx="760" cy="-10" rx="560" ry="95" fill="#4d7aa6" opacity="0.75" filter="url(#soft)"/>
    <ellipse cx="300" cy="600" rx="520" ry="95" fill="#4a76a0" opacity="0.6" filter="url(#soft)"/>
    <line x1="0" y1="390" x2="700" y2="470" stroke="#2c5785" stroke-width="4" opacity="0.8"/>
    <line x1="0" y1="180" x2="820" y2="260" stroke="#2c5785" stroke-width="3" opacity="0.6"/>
  </svg>

  <div class="globe" role="img" aria-label="Illustration eines blauen Globus mit Netzwerklinien und Knotenpunkten"></div>

  <div class="ribbon">
    <h1 class="ribbon-title">Traden für Anfänger</h1>
  </div>

  <svg class="offer-badge" viewBox="0 0 250 235" role="group" aria-label="25 Euro gratis!">
    <defs>
      <linearGradient id="gold" x1="0" y1="0" x2="1" y2="1">
        <stop offset="0" stop-color="var(--gold-light)"/>
        <stop offset="1" stop-color="var(--gold)"/>
      </linearGradient>
    </defs>
    <polygon points="6,102 68,6 200,18 244,125 184,226 52,218"
             fill="url(#gold)" stroke="var(--gold-edge)" stroke-width="4" stroke-linejoin="round"/>
    <g transform="rotate(8 125 118)">
      <text x="125" y="112" text-anchor="middle">25 Euro</text>
      <text x="125" y="170" text-anchor="middle">gratis!</text>
    </g>
  </svg>
</main>
</body>
</html>
```